Stonefield General Contracting Business Card

My company is a General Contracting and Handyman service based in a private community in Northeast Pennsylvania.
Our cliental is a mix of year round and seasonal homeowners
We pride ourselves i using new and innovative building techniques and always try to build with pride and integrity
Please check my website f(under construction) or a list of services and more information
The files below are my logo and my facebook business page profile pic

Industry/Entity Type

Building

Contact Information for Business Card

Stonefield General Contracting
Dale Hurtig
Pine Hollow, Pennsylvania
570-314-2796
dale@stnfldco.com
www.stnfldco.com
www.pagenook.example/stonefieldcontracting

```html
<!DOCTYPE html>
<html lang="en">
<head>
<meta charset="UTF-8">
<title>Stonefield General Contracting – Business Card</title>
<link rel="stylesheet" href="https://fonts.googleapis.com/css2?family=Open+Sans:ital,wght@0,400;0,600;0,700;1,400&family=Roboto:wght@500;700&display=swap">
<style>
  :root {
    --page-bg: #3a3532;
    --card-bg: #1c1c1c;
    --card-bg-deep: #121212;
    --accent: #e8661e;
    --text-light: #f2f2f2;
    --text-muted: #cfcfcf;
    --divider: #8a8a8a;
    --faint-mark: rgba(255, 255, 255, 0.045);
  }
  * { margin: 0; padding: 0; box-sizing: border-box; }
  html, body {
    width: 1200px;
    height: 768px;
    overflow: hidden;
    background: var(--page-bg);
    font-family: "Open Sans", sans-serif;
  }
  .canvas {
    position: relative;
    width: 1200px;
    height: 768px;
  }
  .card {
    position: absolute;
    width: 540px;
    height: 309px;
    background: linear-gradient(135deg, var(--card-bg) 0%, var(--card-bg-deep) 100%);
    box-shadow: 0 10px 30px rgba(0, 0, 0, 0.45);
    overflow: hidden;
  }
  .card-front { left: 50px; top: 110px; }
  .card-back { left: 610px; top: 350px; }

  .tool-decoration {
    position: absolute;
    background: radial-gradient(ellipse at center, var(--faint-mark) 0%, rgba(255,255,255,0) 70%);
  }
  .card-front .tool-decoration { left: 250px; top: 90px; width: 220px; height: 210px; }
  .card-back .tool-decoration { left: 330px; top: 110px; width: 200px; height: 190px; }

  .brand-mark {
    display: flex;
    align-items: center;
    gap: 10px;
    font-family: "Open Sans", sans-serif;
    font-weight: 700;
    color: var(--accent);
  }
  .brand-mark .brand-square {
    width: 22px;
    height: 22px;
    background: var(--accent);
  }
  .card-front .brand-mark {
    position: absolute;
    left: 0; right: 0; top: 128px;
    justify-content: center;
    font-size: 38px;
  }

  .company-block {
    position: absolute;
    left: 34px;
    top: 70px;
    width: 230px;
  }
  .company-block .brand-mark { font-size: 30px; margin-bottom: 18px; }
  .company-name {
    font-family: "Roboto", sans-serif;
    font-weight: 700;
    font-size: 22px;
    color: var(--text-light);
    line-height: 1.1;
  }
  .company-tagline {
    font-size: 15px;
    color: var(--text-light);
    margin-top: 2px;
  }
  .divider {
    position: absolute;
    left: 282px;
    top: 40px;
    width: 1px;
    height: 220px;
    background: var(--divider);
  }
  .person {
    position: absolute;
    left: 302px;
    top: 44px;
  }
  .person-name {
    font-weight: 600;
    font-size: 16px;
    color: var(--accent);
  }
  .person-title {
    font-style: italic;
    font-size: 12px;
    color: var(--text-muted);
  }
  .contact-list {
    position: absolute;
    left: 302px;
    top: 138px;
    list-style: none;
  }
  .contact-list li {
    display: flex;
    align-items: center;
    gap: 10px;
    font-size: 13px;
    line-height: 20px;
    color: var(--text-light);
  }
  .contact-icon {
    width: 11px;
    height: 11px;
    flex: none;
    fill: var(--accent);
  }
  .social-square {
    width: 10px;
    height: 10px;
    background: var(--accent);
    flex: none;
    margin: 0 1px;
  }
</style>
</head>
<body>
<main class="canvas">
  <section class="card card-front" aria-label="Card front">
    <div class="tool-decoration" role="img" aria-label="Faint hammer decoration"></div>
    <div class="brand-mark"><span class="brand-square"></span>Stonefield</div>
  </section>

  <section class="card card-back" aria-label="Card back">
    <div class="tool-decoration" role="img" aria-label="Faint hammer decoration"></div>
    <div class="company-block">
      <div class="brand-mark"><span class="brand-square"></span>Stonefield</div>
      <p class="company-name">Stonefield</p>
      <p class="company-tagline">General Contracting</p>
    </div>
    <div class="divider"></div>
    <div class="person">
      <p class="person-name">Dale Hurtig</p>
      <p class="person-title">Managing Director</p>
    </div>
    <ul class="contact-list">
      <li>
        <svg class="contact-icon" viewBox="0 0 24 24"><path d="M6.6 10.8a15 15 0 0 0 6.6 6.6l2.2-2.2a1 1 0 0 1 1-.25 11.4 11.4 0 0 0 3.6.57 1 1 0 0 1 1 1V20a1 1 0 0 1-1 1A17 17 0 0 1 3 4a1 1 0 0 1 1-1h3.5a1 1 0 0 1 1 1c0 1.25.2 2.45.57 3.6a1 1 0 0 1-.25 1z"/></svg>
        570-314-2796
      </li>
      <li>
        <svg class="contact-icon" viewBox="0 0 24 24"><path d="M2 5h20v14H2z M2 5l10 8 10-8" fill="none" stroke="#e8661e" stroke-width="2.4"/></svg>
        dale@stnfldco.com
      </li>
      <li>
        <svg class="contact-icon" viewBox="0 0 24 24"><circle cx="12" cy="12" r="10" fill="none" stroke="#e8661e" stroke-width="2.4"/><path d="M2 12h20M12 2c3 3 3 17 0 20M12 2c-3 3-3 17 0 20" fill="none" stroke="#e8661e" stroke-width="2"/></svg>
        www.stnfldco.com
      </li>
      <li>
        <svg class="contact-icon" viewBox="0 0 24 24"><path d="M12 2a7 7 0 0 0-7 7c0 5 7 13 7 13s7-8 7-13a7 7 0 0 0-7-7zm0 9.5A2.5 2.5 0 1 1 12 6.5a2.5 2.5 0 0 1 0 5z"/></svg>
        Pine Hollow, Pennsylvania
      </li>
      <li>
        <span class="social-square"></span>
        /stonefieldcontracting
      </li>
    </ul>
  </section>
</main>
</body>
</html>
```